Portal refurbished. We want to provide a new version of an existing website.

Hello,
I would like you inspire yourself form this website: https://tramorivo.com/
The idea is to keep the same mockup but change colors/forms/icons.

Industry/Entity Type

Administration

Number of Pages Required

1 page

Font styles to use
Sans Serif

Requirements
Must have
• Inspire yourself from this website: tramorivo.com, I want to keep the structure
Nice to have
• Nice images and logos so the website is as clear as possible

```html
<!DOCTYPE html>
<html lang="en">
<head>
<meta charset="utf-8">
<title>Tramorivo – Administrative documents, contracts and letter templates</title>
<link href="https://fonts.googleapis.com/css2?family=League+Spartan:wght@400;500;600;700;800&display=swap" rel="stylesheet">
<style>
:root{
  --navy:#0d3352;
  --red:#c8252b;
  --red-dark:#a81d22;
  --sky:#cfe3f0;
  --white:#ffffff;
  --ink:#0d3352;
  --grey:#b9c8d3;
  --slate:#5f7c93;
  --line:#c5ccd3;
}
*{box-sizing:border-box;margin:0;padding:0}
html,body{width:1200px;height:5271px;overflow:hidden}
body{position:relative;font-family:"League Spartan",Arial,sans-serif;color:var(--ink);background:var(--white)}
.abs{position:absolute}

/* header */
.topbar{left:0;top:0;width:1200px;height:45px;background:var(--navy);color:var(--white);font-size:10px;font-weight:600;letter-spacing:.3px}
.topbar .hours{position:absolute;left:317px;top:18px}
.topbar .follow{position:absolute;left:866px;top:18px}
.topbar .dot{position:absolute;top:11px;width:24px;height:24px;border-radius:50%;background:var(--white)}
.brandbox{left:45px;top:0;width:227px;height:133px;background:var(--white);box-shadow:0 4px 14px rgba(0,0,0,.15);z-index:5;display:flex;align-items:center;justify-content:center;flex-direction:column;gap:10px}
.brandbox .mark{width:40px;height:40px;background:var(--navy)}
.brand-name{font-weight:800;font-size:27px;color:var(--navy);letter-spacing:.5px}
.nav{left:317px;top:72px;display:flex;font-size:10px;font-weight:600;text-transform:uppercase}
.nav span{margin-right:36px;position:relative}
.nav .active{color:var(--red)}
.nav .drop::after{content:"";position:absolute;left:50%;top:16px;margin-left:-3px;border:3px solid transparent;border-top-color:var(--navy)}
.subscribe{left:901px;top:61px;width:178px;height:36px;background:var(--navy);color:var(--white);font-size:10px;font-weight:700;display:flex;align-items:center;justify-content:center;text-transform:uppercase}

/* hero */
.hero-photo{left:0;top:113px;width:1200px;height:675px;background:
  radial-gradient(ellipse 260px 300px at 860px 330px,#8a7c73 0%,rgba(138,124,115,0) 100%),
  radial-gradient(ellipse 420px 260px at 900px 620px,#6f6e6e 0%,rgba(111,110,110,0) 100%),
  linear-gradient(90deg,#ffffff 0%,#f2f3f4 28%,#c9c8c5 48%,#9a9794 68%,#b9b5b0 85%,#d8d4cf 100%)}
.hero-title{left:117px;top:297px;font-size:57px;line-height:54px;font-weight:800;color:var(--navy);text-transform:uppercase}
.hero-sub{left:117px;top:475px;font-size:16px;line-height:26px;color:var(--navy);text-transform:uppercase}

/* pricing */
.plan{top:901px;width:470px;height:481px;background:var(--navy);color:var(--white);text-align:center}
.plan .ribbon{margin:19px 14px 0;height:53px;background:linear-gradient(90deg,var(--red),var(--red-dark));font-size:14px;font-weight:700;display:flex;align-items:center;justify-content:center;text-transform:uppercase}
.plan .price{font-size:62px;font-weight:700;margin-top:30px;line-height:62px}
.plan .note{font-size:14px;line-height:22px;margin:22px 40px 0}
.plan .name{font-size:33px;font-weight:700;margin-top:20px;text-transform:uppercase}
.plan .line{font-size:14px;line-height:22px;margin-top:12px}
.plan .cta{position:absolute;left:106px;top:457px;width:258px;height:35px;background:var(--red);font-size:10px;font-weight:700;display:flex;align-items:center;justify-content:center;text-transform:uppercase}

/* section headings */
.band-sky{left:0;width:1200px;background:var(--sky)}
.h2{left:0;width:1200px;text-align:center;font-size:50px;font-weight:800;color:var(--navy);text-transform:uppercase}
.lead{font-size:12.5px;line-height:22px;text-align:center;color:var(--navy)}

/* document previews */
.doc-page{width:190px;height:260px;background:#fbfbfb;box-shadow:0 1px 4px rgba(0,0,0,.12);padding:16px 14px;display:flex;flex-direction:column;gap:6px;overflow:hidden}
.ln{height:4px;background:var(--line);flex:none}
.ln.red{background:var(--red);height:6px}
.ln.navy{background:var(--navy);height:6px}
.ln.c{align-self:center}
.ln.r{align-self:flex-end}
.gap{height:10px;flex:none}
.photo-box{width:60px;height:46px;background:#d9dde1;flex:none}
.doc-card{top:1829px;width:225px;height:284px;background:var(--white);display:flex;align-items:center;justify-content:center}
.doc-card.sel{background:var(--navy)}
.doc-label{top:2133px;width:225px;text-align:center;font-size:12px;font-weight:700;line-height:14px;text-transform:uppercase}
.round-btn{top:1958px;width:24px;height:24px;border-radius:50%;background:var(--white);display:flex;align-items:center;justify-content:center}

/* contracts */
.stack{background:var(--grey)}
.pill{top:3088px;height:35px;color:var(--white);font-size:10px;font-weight:700;display:flex;align-items:center;justify-content:center;text-transform:uppercase}

/* letters */
.tab{top:3512px;width:150px;height:48px;border:2px solid var(--navy);background:var(--white);font-size:10px;font-weight:700;display:flex;align-items:center;justify-content:center;text-transform:uppercase}
.tab.on{background:var(--red);border-color:var(--red);color:var(--white)}
.tpl{top:3625px;width:305px;height:354px;background:var(--white);display:flex;align-items:center;justify-content:center}
.tpl.on{outline:3px solid var(--red);outline-offset:-3px}
.tpl .doc-page{width:270px;height:320px;gap:8px}

/* features */
.feature{top:4285px;width:340px;text-align:center}
.feature .icon{width:106px;height:106px;margin:0 auto;border-radius:50%;background:var(--navy);display:flex;align-items:center;justify-content:center}
.feature h3{font-size:24px;font-weight:700;margin-top:26px;text-transform:uppercase}
.feature p{font-size:18px;line-height:18px;margin-top:8px;text-transform:uppercase}
.vrule{width:2px;background:#b5c3ce}

/* footer */
.footer{left:0;top:4594px;width:1200px;height:677px;background:var(--navy);color:var(--white)}
.footer .logo{position:absolute;left:0;width:1200px;top:245px;text-align:center;font-size:52px;font-weight:700;letter-spacing:1px}
.footer .logo-sq{position:absolute;left:570px;top:165px;width:60px;height:60px;background:var(--white)}
.flist{position:absolute;font-size:13px;line-height:27.5px;list-style:none}
.footer h4{font-size:17px;font-weight:600}
.footer .small{font-size:13px;line-height:27px}
.footer .cards{position:absolute;left:836px;top:520px;font-size:30px;font-weight:700;display:flex;gap:30px}
.footer .rule{position:absolute;left:119px;top:629px;width:960px;height:1px;background:rgba(255,255,255,.6)}
.footer .legal{position:absolute;top:642px;font-size:10.5px}
</style>
</head>
<body>

<!-- header -->
<div class="abs topbar">
  <span class="hours">MONDAY TO FRIDAY FROM 10AM TO 5PM</span>
  <span class="follow">FOLLOW US ON:</span>
  <span class="dot" style="left:978px"></span>
  <span class="dot" style="left:1016px"></span>
  <span class="dot" style="left:1054px"></span>
</div>
<div class="abs brandbox"><span class="mark"></span><span class="brand-name">TRAMORIVO</span></div>
<div class="abs hero-photo" role="img" aria-label="Photo of a woman working on paperwork at an office desk with a laptop"></div>
<div class="abs" style="left:272px;top:45px;width:928px;height:68px;background:var(--white)"></div>
<nav class="abs nav">
  <span class="active">Home</span>
  <span class="drop">Documents</span>
  <span class="drop">Contracts</span>
  <span class="drop">Letter templates</span>
  <span>Contact us</span>
  <span>Access</span>
</nav>
<div class="abs subscribe">My subscription</div>

<h1 class="abs hero-title">For all your<br>administrative<br>needs:</h1>
<p class="abs hero-sub">Administrative documents, contract templates<br>and letter templates</p>

<!-- pricing -->
<div class="abs plan" style="left:119px">
  <div class="ribbon">For the 3 day trial period</div>
  <div class="price">€3.90</div>
  <p class="note">Then automatically renewed as a subscription, for an indefinite time, at €43.90 per month.</p>
  <div class="name">Classic</div>
  <p class="line" style="margin:14px 90px 0">One document during the trial period, then six documents per month</p>
  <p class="line">Unlimited contract downloads</p>
  <p class="line">Unlimited letter template downloads</p>
  <div class="cta">I take this opportunity</div>
</div>
<div class="abs plan" style="left:610px">
  <div class="ribbon">For the 3 day trial period</div>
  <div class="price">€6.90</div>
  <p class="note">Then automatically renewed as a subscription, for an indefinite time, at €43.90 per month.</p>
  <div class="name">Classic +</div>
  <p class="line" style="margin:14px 90px 0">Two document during the trial period, then six documents per month</p>
  <p class="line">Unlimited contract downloads</p>
  <p class="line">Unlimited letter template downloads</p>
  <div class="cta">I take this opportunity</div>
</div>

<!-- administrative documents -->
<section class="abs band-sky" style="top:1509px;height:760px"></section>
<h2 class="abs h2" style="top:1610px">Administrative documents</h2>
<p class="abs lead" style="left:170px;top:1676px;width:860px">Take advantage of our offer to request up to 6 administrative documents per month: Chamber of Commerce Certificate; Land Registry Survey; Credix inspection; Visura Pra; Protest certificate; Full copy of Marriage Certificate; Full copy of Birth Certificate; Chamber of Commerce registration certificate; Family Status Certificate; Rezidencia Certificate. Our teams are committed to providing you with the requested document within 24 hours.</p>

<div class="abs round-btn" style="left:70px"><svg width="10" height="10" viewBox="0 0 10 10"><path d="M6.5 1.5 3 5l3.5 3.5" stroke="#0d3352" stroke-width="1.8" fill="none"/></svg></div>
<div class="abs round-btn" style="left:1109px"><svg width="10" height="10" viewBox="0 0 10 10"><path d="M3.5 1.5 7 5 3.5 8.5" stroke="#0d3352" stroke-width="1.8" fill="none"/></svg></div>

<div class="abs doc-card sel" style="left:119px">
  <div class="doc-page" role="img" aria-label="Preview of a chamber of commerce inspection document">
    <div class="ln" style="width:60%;align-self:flex-end"></div><div class="ln" style="width:50%;align-self:flex-end"></div>
    <div class="ln red"></div><div class="ln" style="width:70%"></div>
    <div class="photo-box"></div>
    <div class="ln" style="width:90%"></div><div class="ln" style="width:80%"></div>
    <div class="ln red"></div><div class="ln"></div><div class="ln" style="width:85%"></div><div class="ln" style="width:75%"></div>
    <div class="ln red"></div><div class="ln" style="width:90%"></div><div class="ln" style="width:60%"></div><div class="ln" style="width:80%"></div>
  </div>
</div>
<div class="abs doc-card" style="left:365px">
  <div class="doc-page" role="img" aria-label="Preview of a chamber of commerce registration certificate">
    <div class="ln c" style="width:40%"></div><div class="ln c" style="width:60%"></div><div class="gap"></div>
    <div class="ln" style="width:70%"></div><div class="ln" style="width:85%"></div><div class="ln" style="width:55%"></div>
    <div class="gap"></div><div class="ln" style="width:90%"></div><div class="ln" style="width:75%"></div><div class="ln" style="width:65%"></div>
    <div class="gap"></div><div class="ln" style="width:80%"></div><div class="ln" style="width:50%"></div>
  </div>
</div>
<div class="abs doc-card" style="left:610px">
  <div class="doc-page" role="img" aria-label="Preview of a family status certificate">
    <div class="ln navy" style="width:35%"></div><div class="gap"></div>
    <div class="ln" style="width:60%"></div><div class="ln" style="width:45%"></div><div class="ln" style="width:70%"></div>
    <div class="ln" style="width:55%"></div><div class="ln" style="width:65%"></div><div class="ln" style="width:40%"></div>
    <div class="ln" style="width:60%"></div><div class="ln" style="width:50%"></div><div class="gap"></div>
    <div class="ln" style="width:75%"></div><div class="ln" style="width:45%"></div>
  </div>
</div>
<div class="abs doc-card" style="left:856px">
  <div class="doc-page" role="img" aria-label="Preview of a full copy of marriage certificate">
    <div class="ln c" style="width:30%"></div><div class="ln c" style="width:75%"></div><div class="gap"></div>
    <div class="ln" style="width:55%"></div><div class="ln" style="width:65%"></div><div class="ln" style="width:45%"></div>
    <div class="gap"></div><div class="ln"></div><div class="ln" style="width:90%"></div><div class="ln" style="width:70%"></div>
    <div class="ln r" style="width:40%"></div><div class="gap"></div><div class="ln"></div><div class="ln" style="width:85%"></div>
  </div>
</div>
<div class="abs doc-label" style="left:119px">Chambers of commerce<br>inspection</div>
<div class="abs doc-label" style="left:365px">Chambers of commerce<br>registration certificate</div>
<div class="abs doc-label" style="left:610px">Family status<br>certificates</div>
<div class="abs doc-label" style="left:856px">Full copy of marriage<br>certificates</div>

<!-- contracts -->
<h2 class="abs h2" style="top:2372px">Contracts</h2>
<p class="abs lead" style="left:0;top:2440px;width:1200px">Download our contract templates, regularly updated, unlimited. It also benefits, in particular, from English templates for professionals.</p>

<div class="abs stack" style="left:137px;top:2566px;width:932px;height:424px"></div>
<div class="abs" style="left:215px;top:2543px;width:774px;height:472px;background:var(--slate)"></div>
<div class="abs" style="left:268px;top:2515px;width:650px;height:516px;background:var(--navy)"></div>
<div class="abs doc-page" style="left:438px;top:2550px;width:324px;height:456px;background:#fff;padding:40px 38px;gap:8px" role="img" aria-label="Preview of a contract template page">
  <div class="ln c" style="width:25%"></div><div class="gap"></div>
  <div class="ln"></div><div class="ln" style="width:90%"></div><div class="ln" style="width:40%"></div><div class="gap"></div>
  <div class="ln"></div><div class="ln" style="width:85%"></div><div class="gap"></div>
  <div class="ln"></div><div class="ln" style="width:70%"></div><div class="gap"></div>
  <div class="ln" style="width:95%"></div><div class="ln" style="width:30%"></div><div class="gap"></div>
  <div class="ln r" style="width:20%"></div><div class="ln r" style="width:15%"></div><div class="gap"></div>
  <div class="ln" style="width:20%"></div><div class="ln" style="width:18%"></div><div class="ln" style="width:30%"></div>
</div>

<svg class="abs" style="left:57px;top:2748px" width="56" height="60" viewBox="0 0 56 60">
  <path d="M0 2h26M0 17h56M0 32h26M0 47h26" stroke="#c8252b" stroke-width="2"/>
  <path d="M0 17h26" stroke="#5f7c93" stroke-width="2"/>
</svg>
<svg class="abs" style="left:1094px;top:2752px" width="52" height="40" viewBox="0 0 52 40">
  <path d="M0 10h50M42 3l8 7-8 7" stroke="#c8252b" stroke-width="2" fill="none"/>
  <path d="M52 32H2M10 25l-8 7 8 7" stroke="#5f7c93" stroke-width="2" fill="none"/>
</svg>

<div class="abs pill" style="left:346px;width:242px;background:var(--navy)">English contracts</div>
<div class="abs pill" style="left:608px;width:244px;background:var(--red)">Italian contracts</div>

<!-- letter templates -->
<section class="abs band-sky" style="top:3236px;height:936px"></section>
<h2 class="abs" style="left:119px;top:3343px;font-size:49px;line-height:50px;font-weight:800;text-transform:uppercase">Letter<br>templates</h2>
<div class="abs vrule" style="left:581px;top:3318px;height:149px;background:var(--navy)"></div>
<p class="abs" style="left:715px;top:3364px;width:370px;font-size:11.5px;line-height:23px">Download our letter templates, regularly updated, without limits. Letter templates for work, family, insurance ... etc. For all your needs</p>

<div class="abs tab on" style="left:113px">Insurance</div>
<div class="abs tab" style="left:277px">Consumers</div>
<div class="abs tab" style="left:442px">Family</div>
<div class="abs tab" style="left:606px">Real esatate</div>
<div class="abs tab" style="left:772px">Work</div>
<div class="abs tab" style="left:936px">Money</div>

<div class="abs tpl on" style="left:119px">
  <div class="doc-page" role="img" aria-label="Preview of an insurance letter template">
    <div class="ln r" style="width:55%"></div><div class="ln r" style="width:45%"></div>
    <div class="ln red"></div><div class="photo-box" style="width:80px;height:60px"></div>
    <div class="ln" style="width:80%"></div><div class="ln" style="width:65%"></div>
    <div class="ln red"></div><div class="ln"></div><div class="ln" style="width:85%"></div><div class="ln" style="width:70%"></div>
    <div class="ln red"></div><div class="ln" style="width:90%"></div><div class="ln" style="width:60%"></div><div class="ln" style="width:75%"></div>
  </div>
</div>
<div class="abs tpl" style="left:446px">
  <div class="doc-page" role="img" aria-label="Preview of an insurance letter template">
    <div class="ln navy" style="width:30%"></div><div class="gap"></div>
    <div class="ln" style="width:50%"></div><div class="ln" style="width:40%"></div><div class="ln" style="width:60%"></div>
    <div class="ln" style="width:45%"></div><div class="ln" style="width:55%"></div><div class="ln" style="width:35%"></div>
    <div class="ln" style="width:50%"></div><div class="ln" style="width:40%"></div><div class="gap"></div>
    <div class="ln" style="width:70%"></div><div class="ln" style="width:45%"></div>
  </div>
</div>
<div class="abs tpl" style="left:774px">
  <div class="doc-page" role="img" aria-label="Preview of an insurance letter template">
    <div class="ln r" style="width:30%"></div><div class="ln red"></div><div class="gap"></div>
    <div class="ln r" style="width:60%"></div><div class="ln r" style="width:50%"></div><div class="gap"></div>
    <div class="ln" style="width:35%"></div><div class="ln" style="width:45%"></div><div class="ln" style="width:40%"></div>
    <div class="gap"></div><div class="ln"></div><div class="ln" style="width:80%"></div>
  </div>
</div>
<div class="abs" style="left:404px;top:3607px;width:36px;height:36px;border-radius:50%;background:var(--red);color:#fff;font-size:17px;font-weight:700;display:flex;align-items:center;justify-content:center">1</div>

<div class="abs pill" style="left:471px;top:4022px;width:258px;height:37px;background:var(--red)">Select to download
  <svg style="margin-left:24px" width="14" height="14" viewBox="0 0 14 14"><path d="M7 1v8M3.5 6 7 9.5 10.5 6M1 13h12" stroke="#fff" stroke-width="1.6" fill="none"/></svg>
</div>

<!-- features -->
<div class="abs vrule" style="left:414px;top:4306px;height:150px"></div>
<div class="abs vrule" style="left:754px;top:4306px;height:150px"></div>
<div class="abs feature" style="left:74px">
  <div class="icon"><svg width="50" height="40" viewBox="0 0 50 40"><rect x="2" y="6" width="38" height="26" rx="3" fill="none" stroke="#fff" stroke-width="3"/><path d="M2 14h38" stroke="#fff" stroke-width="4"/><path d="M30 26l5 5 11-11" stroke="#fff" stroke-width="3.5" fill="none"/></svg></div>
  <h3>Secure payment:</h3>
  <p>Cardiva and Paynetra</p>
</div>
<div class="abs feature" style="left:414px">
  <div class="icon"><svg width="46" height="46" viewBox="0 0 46 46"><circle cx="23" cy="17" r="11" fill="none" stroke="#fff" stroke-width="3"/><path d="M18 17l4 4 7-8" stroke="#fff" stroke-width="3" fill="none"/><path d="M5 36c8 0 10-4 18-4s8 4 18 4" stroke="#fff" stroke-width="3" fill="none"/></svg></div>
  <h3>Quality service:</h3>
  <p>For individuals and<br>professionals.</p>
</div>
<div class="abs feature" style="left:770px">
  <div class="icon"><svg width="46" height="46" viewBox="0 0 46 46"><path d="M9 24v-4a14 14 0 0 1 28 0v4" stroke="#fff" stroke-width="3" fill="none"/><rect x="6" y="22" width="7" height="12" rx="3" fill="#fff"/><rect x="33" y="22" width="7" height="12" rx="3" fill="#fff"/><path d="M36 34c0 5-6 7-12 7" stroke="#fff" stroke-width="3" fill="none"/></svg></div>
  <h3>Customer service:</h3>
  <p>Available 7 days a week</p>
</div>

<!-- footer -->
<footer class="abs footer">
  <div class="logo-sq"></div>
  <div class="logo">TRAMORIVO</div>
  <ul class="flist" style="left:119px;top:400px">
    <li>Home page</li><li>Classic</li><li>Classic +</li><li>Italian contracts</li><li>English Contracts</li><li>Letters</li>
  </ul>
  <ul class="flist" style="left:336px;top:428px">
    <li>Terms of Service</li><li>Privacy policy</li><li>Cookie policy</li><li>Legal notices</li>
  </ul>
  <div style="position:absolute;left:516px;top:405px;height:175px;width:1px;background:#fff"></div>
  <div style="position:absolute;left:549px;top:450px">
    <h4>Contacts</h4>
    <p class="small">contact@tramorivo.com<br>Opening hours: 10am - 5pm</p>
  </div>
  <div style="position:absolute;left:784px;top:405px;height:175px;width:1px;background:#fff"></div>
  <div style="position:absolute;left:836px;top:418px">
    <h4>Our teams at your service</h4>
    <p class="small">Monday to Friday from 10am to 5pm</p>
  </div>
  <div class="cards"><span>Paynetra</span><span>CARDIVA</span></div>
  <div class="rule"></div>
  <span class="legal" style="left:122px">© tramorivo.com 2020</span>
  <span class="legal" style="left:395px">Norvale Web Services Limited</span>
  <span class="legal" style="left:690px">Harlow Court, 12 - 14, Greater London, United Kingdom, SE9 4QP</span>
</footer>

</body>
</html>
```